automatic Real Estate Sales Brochure

Print-out of 3 to 8 pages automatically on a color inkjet printer. Page size A4
All details for my Real Estate Sales Design Project are in attached file.
Here some points:
We have abound 100 real estate objects for sale (houses, flats and pieces of land).
For each item, our system creates automatically a sales documentation, which we print out and hand to the potential buyers after they've visited the object or send it by mail upon request in form of a pdf.
This document should be of 3 to maximum 8 pages.
It should be of a modern design and invite the client to read it.
The information should be clear and quick to find.
If the global look could somehow relate to the look of our web site www.norvelhaus.ch, that would be nice.
The company data is there for legal reasons, but it is the agent's phone and mail that the clients should use for contact.
The photos should be of big size (2 by page?) without being distorted nor cut.
Optionally, to save ink and pages, maybe only the first 3-4 photos full size and the rest smaller?

Target Market(s)

will be printed or sent as PDF "on the fly", meaning no pre-printing at a print shop!

Industry/Entity Type

Real Estate

Font styles to use
Sans Serif

Requirements
Must have
• see details in attached file
Should not have
• no edge-to-edge printing
• no double-page printing (A3)

```html
<!DOCTYPE html>
<html lang="fr">
<head>
<meta charset="utf-8">
<title>NorvelHaus – Dossier de vente</title>
<link href="https://fonts.googleapis.com/css2?family=Montserrat:wght@700;800&family=Lato:wght@400;700&family=Quicksand:wght@500;700&display=swap" rel="stylesheet">
<style>
:root{
  --bg:#ecebe8;
  --paper:#ffffff;
  --pink:#ef5f6b;
  --red:#e0262f;
  --ink:#333;
  --grey:#8b8b8b;
  --greyband:#9a9a9a;
  --light:#f1f1f1;
}
*{margin:0;padding:0;box-sizing:border-box}
html,body{width:1200px;height:1200px;overflow:hidden;background:var(--bg)}
.page{position:absolute;top:218px;width:539px;height:763px;background:var(--paper);box-shadow:0 4px 14px rgba(0,0,0,.18);font-family:"Lato",sans-serif;color:var(--ink)}
.page--one{left:48px}
.page--two{left:613px}
.abs{position:absolute}
.brand{position:absolute;left:0;right:0;text-align:center;font-family:"Montserrat",sans-serif;font-weight:800;color:var(--red);letter-spacing:.5px}
.page--one .brand{top:26px;font-size:40px}
.page--two .brand{top:24px;font-size:30px}
.rule{position:absolute;left:0;right:0;top:95px;height:1px;background:#bbb}
.photo{position:absolute}
.hero{left:0;right:0;top:96px;height:336px;background:linear-gradient(160deg,#cfe0ea 0%,#9fae7a 30%,#e8dcc4 60%,#d9b98f 100%)}
.hero-band{position:absolute;left:0;right:0;top:434px;height:137px;background:var(--pink);color:#fff;text-align:center}
.hero-band .title1{position:absolute;left:0;right:0;top:24px;font-family:"Montserrat",sans-serif;font-weight:800;font-size:18px}
.hero-band .title2{position:absolute;left:0;right:0;top:48px;font-family:"Montserrat",sans-serif;font-weight:800;font-size:31px}
.hero-band .agent{position:absolute;left:0;right:0;top:96px;font-family:"Quicksand",sans-serif;font-weight:700;font-size:16px}
.hero-band .agent span{margin:0 7px}
.specs{position:absolute;left:0;right:0;top:571px;height:131px;background:linear-gradient(#fafafa,#eee)}
.cell{position:absolute;height:13px;background:var(--greyband);color:#fff;font-family:"Quicksand",sans-serif;font-weight:700;font-size:8px;line-height:13px;padding-left:6px;text-transform:uppercase}
.footer{position:absolute;left:0;right:0;top:702px;height:41px;background:var(--pink);color:#fff;font-family:"Quicksand",sans-serif;font-weight:700}
.footer .co{position:absolute;left:47px;top:7px;font-size:11px}
.footer .addr{position:absolute;left:47px;top:24px;font-size:9px}
.footer .mail{position:absolute;left:257px;top:8px;font-size:9px;line-height:14px}
.footer .tel{position:absolute;left:447px;top:8px;font-size:9px;line-height:14px}
.footer svg{position:absolute}
h2{position:absolute;font-family:"Quicksand",sans-serif;font-weight:700;color:var(--pink);font-size:16px;letter-spacing:.3px}
.desc{position:absolute;left:33px;top:124px;width:289px;font-size:7px;line-height:8.4px;text-align:justify;color:#444}
.desc p{margin-bottom:8.4px}
.portrait{left:341px;top:123px;width:165px;height:183px;border:1px solid #ddd;background:linear-gradient(#f4f4f4,#cfc6c0)}
.namebar{position:absolute;left:341px;top:307px;width:165px;height:22px;background:var(--pink);color:#fff;text-align:center;font-family:"Quicksand",sans-serif;font-weight:700;font-size:15px;line-height:22px}
.agentphone{position:absolute;left:341px;top:332px;width:165px;text-align:center;font-family:"Quicksand",sans-serif;font-weight:500;font-size:16px;color:#444}
.divider{position:absolute;left:156px;right:33px;top:395px;height:1px;background:#ccc}
.amen{position:absolute;font-size:9.5px;color:#333}
.amen b{font-weight:400;color:var(--red);text-transform:uppercase;font-family:"Quicksand",sans-serif;font-weight:700}
.thumb{top:539px;height:143px;width:146px;border:1px solid #ddd;background:linear-gradient(#f1ede6 0%,#e7e1d6 55%,#c8843e 56%,#b36f2e 100%)}
</style>
</head>
<body>

<section class="page page--one">
  <div class="brand">NorvelHaus</div>
  <div class="rule"></div>
  <div class="photo hero" role="img" aria-label="Photo du balcon arrondi donnant sur un parc arboré"></div>
  <div class="hero-band">
    <div class="title1">LUMINEUX 4.5 DE 100M2 IDÉALEMENT SITUÉ !</div>
    <div class="title2">A 1200 GENÈVE</div>
    <div class="agent">Votre courtier<span>|</span>Claire Vautier<span></span>
      <svg width="14" height="14" viewBox="0 0 24 24" style="vertical-align:-2px;margin-right:8px"><path fill="none" stroke="#fff" stroke-width="2" d="M6 3l3 4-2 2c1 3 4 6 7 7l2-2 4 3-2 3C10 20 4 14 3 5z"/></svg>0770 001 122</div>
  </div>
  <div class="specs">
    <div class="cell" style="left:32px;top:39px;width:128px">Type de bien</div>
    <div class="cell" style="left:168px;top:39px;width:98px">Appartement</div>
    <div class="cell" style="left:274px;top:39px;width:128px">Prix</div>
    <div class="cell" style="left:409px;top:39px;width:98px">895 000.-</div>
    <div class="cell" style="left:32px;top:58px;width:128px">Surface habitable m2</div>
    <div class="cell" style="left:168px;top:58px;width:98px">100 m²</div>
    <div class="cell" style="left:274px;top:58px;width:128px">Année de</div>
    <div class="cell" style="left:409px;top:58px;width:98px">1994</div>
    <div class="cell" style="left:32px;top:76px;width:128px">Nombre de pièces</div>
    <div class="cell" style="left:168px;top:76px;width:98px">4,5</div>
    <div class="cell" style="left:274px;top:76px;width:128px">Etat</div>
    <div class="cell" style="left:409px;top:76px;width:98px">Bon état</div>
    <div class="cell" style="left:32px;top:94px;width:128px">Surface parcelle m2</div>
    <div class="cell" style="left:168px;top:94px;width:98px">0 m²</div>
    <div class="cell" style="left:274px;top:94px;width:128px">Libre dès le</div>
    <div class="cell" style="left:409px;top:94px;width:98px"></div>
  </div>
  <div class="footer">
    <svg style="left:31px;top:8px" width="10" height="10" viewBox="0 0 10 10"><path fill="#fff" d="M5 0L10 5H8.5V10H6V7H4V10H1.5V5H0z"/></svg>
    <div class="co">NORVELHAUS SÀRL</div>
    <div class="addr">Rue des Tilleuls 7, 1806 Corsier</div>
    <svg style="left:237px;top:10px" width="11" height="8" viewBox="0 0 11 8"><rect x=".5" y=".5" width="10" height="7" fill="none" stroke="#fff"/><path d="M.5 .5L5.5 4.5 10.5 .5" fill="none" stroke="#fff"/></svg>
    <svg style="left:237px;top:24px" width="10" height="10" viewBox="0 0 10 10"><circle cx="5" cy="5" r="4.3" fill="none" stroke="#fff"/><path d="M.7 5h8.6M5 .7c-2 2.5-2 6 0 8.6M5 .7c2 2.5 2 6 0 8.6" fill="none" stroke="#fff" stroke-width=".8"/></svg>
    <div class="mail">INFO@NORVELHAUS.CH<br>WWW.NORVELHAUS.CH</div>
    <svg style="left:434px;top:10px" width="9" height="9" viewBox="0 0 24 24"><path fill="none" stroke="#fff" stroke-width="3" d="M6 3l3 4-2 2c1 3 4 6 7 7l2-2 4 3-2 3C10 20 4 14 3 5z"/></svg>
    <svg style="left:434px;top:24px" width="9" height="9" viewBox="0 0 10 10"><rect x="1" y="3" width="8" height="6" fill="none" stroke="#fff"/><rect x="3" y="1" width="4" height="3" fill="#fff"/></svg>
    <div class="tel">021 555 01 42<br>021 555 01 43</div>
  </div>
</section>

<section class="page page--two">
  <div class="brand">NorvelHaus</div>
  <h2 style="left:31px;top:96px">DESCRIPTION :</h2>
  <div class="desc">
    <p>Venez visiter sans tarder ce bel appartement situé dans un environnement calme et vert tout en étant proche du centre ville et de toutes les commodités. Il profite de beaux volumes et de pièces de vie très lumineuses. Au 1er étage d'une copropriété soignée, c'est le bien idéal pour un couple ou une famille.</p>
    <p>Cet appartement pourrait aussi convenir comme investissement pour un client souhaitant le louer.</p>
    <p>Il est en bon état d'entretien et se réjouit d'accueillir ses nouveaux propriétaires !</p>
    <p>Il se distribue ainsi</p>
    <p>Une entrée avec armoire encastrée dessert de part et d'autre la partie jour et la partie nuit. La spacieuse pièce de vie se compose d'une cuisine ouverte entièrement équipée et aménagée s'ouvrant sur le séjour. Il profite d'une exposition optimale. Du séjour, vous avez accès à un agréable balcon qui offre une belle vue dégagée sur un environnement verdoyant.</p>
    <p>La partie nuit offre trois belles chambres, une salle de bains avec baignoire, lavabo, wc ainsi qu'un wc visiteurs.</p>
    <p>Deux places de parc intérieures en sus s'ajoutent à ce bel appartement. N'hésitez pas, contactez-moi pour plus d'informations et pour une visite !</p>
  </div>
  <div class="photo portrait" role="img" aria-label="Portrait de la courtière"></div>
  <div class="namebar">Claire Vautier</div>
  <div class="agentphone"><svg width="15" height="15" viewBox="0 0 24 24" style="vertical-align:-2px;margin-right:4px"><path fill="none" stroke="#444" stroke-width="2" d="M6 3l3 4-2 2c1 3 4 6 7 7l2-2 4 3-2 3C10 20 4 14 3 5z"/></svg>0770 001 122</div>

  <h2 style="left:33px;top:378px">COMMODITÉS :</h2>
  <div class="divider"></div>
  <div class="amen" style="left:33px;top:411px"><b>Etage :</b> 1er étage</div>
  <div class="amen" style="left:33px;top:432px"><b>Vue :</b> vue dégagée sur le parc</div>
  <div class="amen" style="left:33px;top:453px"><b>Commerces :</b> à proximité immédiate</div>
  <div class="amen" style="left:33px;top:474px"><b>Ecoles :</b> Collège des Vergers</div>
  <div class="amen" style="left:33px;top:495px"><b>Transports publics :</b> à 5 minutes à pied</div>
  <div class="amen" style="left:334px;top:411px"><b>Chauffage :</b> mazout / au sol</div>
  <div class="amen" style="left:334px;top:432px"><b>Cave :</b> oui</div>
  <div class="amen" style="left:334px;top:453px"><b>Garage :</b> 2 places de parc intérieures</div>
  <div class="amen" style="left:334px;top:474px"><b>Balcon :</b> oui</div>
  <div class="amen" style="left:334px;top:495px"><b>Ascenseur :</b> oui</div>

  <div class="photo thumb" style="left:33px" role="img" aria-label="Photo du séjour avec parquet et porte-fenêtre"></div>
  <div class="photo thumb" style="left:196px" role="img" aria-label="Photo de la cuisine ouverte équipée"></div>
  <div class="photo thumb" style="left:361px" role="img" aria-label="Photo d'une pièce lumineuse avec parquet"></div>

  <div class="footer">
    <svg style="left:31px;top:8px" width="10" height="10" viewBox="0 0 10 10"><path fill="#fff" d="M5 0L10 5H8.5V10H6V7H4V10H1.5V5H0z"/></svg>
    <div class="co">NORVELHAUS SÀRL</div>
    <div class="addr">Rue des Tilleuls 7, 1806 Corsier</div>
    <svg style="left:237px;top:10px" width="11" height="8" viewBox="0 0 11 8"><rect x=".5" y=".5" width="10" height="7" fill="none" stroke="#fff"/><path d="M.5 .5L5.5 4.5 10.5 .5" fill="none" stroke="#fff"/></svg>
    <svg style="left:237px;top:24px" width="10" height="10" viewBox="0 0 10 10"><circle cx="5" cy="5" r="4.3" fill="none" stroke="#fff"/><path d="M.7 5h8.6M5 .7c-2 2.5-2 6 0 8.6M5 .7c2 2.5 2 6 0 8.6" fill="none" stroke="#fff" stroke-width=".8"/></svg>
    <div class="mail">INFO@NORVELHAUS.CH<br>WWW.NORVELHAUS.CH</div>
    <svg style="left:434px;top:10px" width="9" height="9" viewBox="0 0 24 24"><path fill="none" stroke="#fff" stroke-width="3" d="M6 3l3 4-2 2c1 3 4 6 7 7l2-2 4 3-2 3C10 20 4 14 3 5z"/></svg>
    <svg style="left:434px;top:24px" width="9" height="9" viewBox="0 0 10 10"><rect x="1" y="3" width="8" height="6" fill="none" stroke="#fff"/><rect x="3" y="1" width="4" height="3" fill="#fff"/></svg>
    <div class="tel">021 555 01 42<br>021 555 01 43</div>
  </div>
</section>

</body>
</html>
```